PEAK KENNEL - business card
A way to remember us and buy our products
Professional
PEAKKENNEL - the finest pick
Lindmarkv. 24
SE-712 46 Brovika
SWEDEN
info@peakkennel-demo.se
www.peakkennel-demo.se
I would like the business cards and other material to match.
It is about dogs and our show trolley.
I need something to hand out as I meet people at dog shows or otherwise.
your ideas are welcome to figure out what the backside should be.
drawing of product_logo related
LOGO in whole, van be split into two
4 berth
LOGO PDF
drawing pdf
Product today. Steel 2 berth

```html
<!DOCTYPE html>
<html lang="en">
<head>
<meta charset="utf-8">
<title>PEAK KENNEL – Stationery</title>
<link rel="stylesheet" href="https://fonts.googleapis.com/css2?family=Montserrat:wght@400;700&display=swap">
<style>
  :root {
    --orange: #f39200;
    --blue: #1d5a8e;
    --blue-dark: #154670;
    --paper: #ffffff;
    --backdrop: #e9e7e3;
    --ink-soft: #8a95a3;
    --ink: #4a5563;
    --mark-faint: #eef1f5;
  }
  * { box-sizing: border-box; margin: 0; padding: 0; }
  html, body { width: 1200px; height: 310px; overflow: hidden; }
  body {
    position: relative;
    background: var(--backdrop);
    font-family: "Montserrat", Arial, sans-serif;
  }
  .piece {
    position: absolute;
    background: var(--paper);
    box-shadow: 0 1px 3px rgba(0,0,0,.18);
    overflow: hidden;
  }
  .brand {
    display: flex; align-items: center; gap: 4px;
    color: var(--blue); font-weight: 700; letter-spacing: .02em;
    white-space: nowrap;
  }
  .brand-square { background: var(--orange); flex: none; }
  .tagline { color: var(--ink-soft); font-size: 5px; letter-spacing: .05em; }
  .wave { position: absolute; left: 0; bottom: 0; width: 100%; }
  .footer-text {
    position: absolute; left: 0; right: 0; bottom: 3px;
    text-align: center; font-size: 3.2px; color: var(--paper); white-space: nowrap;
  }
  .faint-mark {
    position: absolute; border-radius: 50%; background: var(--mark-faint);
  }

  /* Primary logo */
  .logo-main { position: absolute; left: 14px; top: 62px; }
  .logo-main .brand { font-size: 22px; gap: 8px; }
  .logo-main .brand-square { width: 26px; height: 26px; }
  .logo-main .tagline { font-size: 7px; margin: 4px 0 0 34px; }

  /* Business card front */
  .card-front { left: 18px; top: 150px; width: 108px; height: 64px; }
  .card-front .brand { position: absolute; left: 7px; top: 7px; font-size: 7.5px; gap: 3px; }
  .card-front .brand-square { width: 8px; height: 8px; }
  .card-front .tagline { position: absolute; left: 18px; top: 17px; font-size: 4px; }
  .card-contact {
    position: absolute; left: 7px; top: 26px;
    font-size: 3.6px; line-height: 1.45; color: var(--ink); white-space: nowrap;
  }
  .card-product {
    position: absolute; right: 7px; top: 22px; width: 28px; height: 30px;
    background: linear-gradient(160deg, var(--mark-faint), #c9d3df);
    border-radius: 2px;
  }
  .card-front .wave { height: 8px; }

  /* Business card backs */
  .card-back-art {
    left: 18px; top: 226px; width: 54px; height: 54px;
    background: linear-gradient(135deg, var(--blue) 0 45%, var(--orange) 45% 70%, var(--blue-dark) 70%);
  }
  .card-back-plain {
    left: 78px; top: 226px; width: 56px; height: 54px; background: var(--blue);
    display: flex; align-items: center; justify-content: center;
  }
  .card-back-plain span { width: 18px; height: 18px; background: var(--orange); }

  /* Letterheads */
  .letterhead { top: 40px; width: 190px; height: 262px; }
  .letterhead-one { left: 270px; }
  .letterhead-two { left: 484px; }
  .letterhead .brand { position: absolute; left: 14px; top: 14px; font-size: 9px; }
  .letterhead .brand-square { width: 10px; height: 10px; }
  .letterhead .faint-mark { width: 100px; height: 100px; left: 45px; top: 70px; }
  .letterhead .wave { height: 30px; }

  /* DL envelopes */
  .envelope { left: 690px; width: 190px; }
  .envelope-one { top: 96px; height: 88px; }
  .envelope-two { top: 206px; height: 88px; }
  .envelope .brand { position: absolute; left: 10px; top: 9px; font-size: 7px; }
  .envelope .brand-square { width: 8px; height: 8px; }
  .envelope .faint-mark { width: 46px; height: 46px; left: 72px; top: 16px; }
  .envelope .wave { height: 18px; }

  /* Envelope backs */
  .env-back { left: 924px; width: 250px; height: 58px; }
  .env-back svg { position: absolute; inset: 0; width: 100%; height: 100%; }
  .env-back .seal {
    position: absolute; left: 117px; top: 14px; width: 16px; height: 16px;
  }
  .seal-blue { background: var(--blue); }
  .seal-orange { background: var(--orange); }
  .env-back-orange { top: 46px; }
  .env-back-blue { top: 112px; }
  .env-back-white { top: 178px; }
</style>
</head>
<body>

  <section class="logo-main">
    <div class="brand"><span class="brand-square"></span>PEAKKENNEL</div>
    <p class="tagline">Show Trolleys</p>
  </section>

  <section class="piece card-front">
    <div class="brand"><span class="brand-square"></span>PEAKKENNEL</div>
    <p class="tagline">Show Trolleys</p>
    <address class="card-contact" style="font-style: normal">
      Lindmarkv. 24<br>
      SE-712 46 Brovika, SWEDEN<br>
      info@peakkennel-demo.se<br>
      www.peakkennel-demo.se
    </address>
    <div class="card-product" role="img" aria-label="Product image of the dog show trolley"></div>
    <svg class="wave" viewBox="0 0 108 8" preserveAspectRatio="none">
      <path d="M0 4 C30 1 70 7 108 2 L108 8 L0 8 Z" fill="var(--orange)"/>
      <path d="M0 5.5 C35 2 72 8 108 3.5 L108 8 L0 8 Z" fill="var(--blue)"/>
    </svg>
  </section>
  <div class="piece card-back-art" role="img" aria-label="Card back artwork with show trolley illustration in blue and orange"></div>
  <div class="piece card-back-plain"><span></span></div>

  <section class="piece letterhead letterhead-one">
    <div class="brand"><span class="brand-square"></span>PEAKKENNEL</div>
    <div class="faint-mark"></div>
    <svg class="wave" viewBox="0 0 190 30" preserveAspectRatio="none">
      <path d="M0 14 C50 4 110 22 190 8 L190 30 L0 30 Z" fill="var(--orange)"/>
      <path d="M0 18 C60 8 120 26 190 12 L190 30 L0 30 Z" fill="var(--blue)"/>
    </svg>
    <p class="footer-text">Lindmarkv. 24 · SE-712 46 Brovika · info@peakkennel-demo.se · www.peakkennel-demo.se</p>
  </section>

  <section class="piece letterhead letterhead-two">
    <div class="brand"><span class="brand-square"></span>PEAKKENNEL</div>
    <div class="faint-mark"></div>
    <svg class="wave" viewBox="0 0 190 30" preserveAspectRatio="none">
      <path d="M0 14 C50 4 110 22 190 8 L190 30 L0 30 Z" fill="var(--orange)"/>
      <path d="M0 18 C60 8 120 26 190 12 L190 30 L0 30 Z" fill="var(--blue)"/>
    </svg>
    <p class="footer-text">Lindmarkv. 24 · SE-712 46 Brovika · info@peakkennel-demo.se · www.peakkennel-demo.se</p>
  </section>

  <section class="piece envelope envelope-one">
    <div class="brand"><span class="brand-square"></span>PEAKKENNEL</div>
    <div class="faint-mark"></div>
    <svg class="wave" viewBox="0 0 190 18" preserveAspectRatio="none">
      <path d="M0 8 C50 2 110 14 190 4 L190 18 L0 18 Z" fill="var(--orange)"/>
      <path d="M0 11 C60 4 120 16 190 7 L190 18 L0 18 Z" fill="var(--blue)"/>
    </svg>
  </section>

  <section class="piece envelope envelope-two">
    <div class="brand"><span class="brand-square"></span>PEAKKENNEL</div>
    <div class="faint-mark"></div>
    <svg class="wave" viewBox="0 0 190 18" preserveAspectRatio="none">
      <path d="M0 8 C50 2 110 14 190 4 L190 18 L0 18 Z" fill="var(--orange)"/>
      <path d="M0 11 C60 4 120 16 190 7 L190 18 L0 18 Z" fill="var(--blue)"/>
    </svg>
  </section>

  <section class="piece env-back env-back-orange">
    <svg viewBox="0 0 250 58" preserveAspectRatio="none">
      <path d="M0 0 L250 0 L250 10 L125 40 L0 10 Z" fill="var(--orange)"/>
      <path d="M0 58 L125 30 L250 58" fill="none" stroke="#dde2e8" stroke-width="1"/>
    </svg>
    <span class="seal seal-blue"></span>
  </section>

  <section class="piece env-back env-back-blue">
    <svg viewBox="0 0 250 58" preserveAspectRatio="none">
      <path d="M0 0 L250 0 L250 10 L125 40 L0 10 Z" fill="var(--blue)"/>
      <path d="M0 58 L125 30 L250 58" fill="none" stroke="#dde2e8" stroke-width="1"/>
    </svg>
    <span class="seal seal-orange"></span>
  </section>

  <section class="piece env-back env-back-white">
    <svg viewBox="0 0 250 58" preserveAspectRatio="none">
      <path d="M0 0 L250 0 L250 10 L125 40 L0 10 Z" fill="#f6f7f9" stroke="#dde2e8" stroke-width="1"/>
      <path d="M0 58 L125 30 L250 58" fill="none" stroke="#dde2e8" stroke-width="1"/>
    </svg>
    <span class="seal seal-orange"></span>
  </section>

</body>
</html>
```